New Vegan Documentary Film Needs Poster Design

We are developing a documentary film production project called "Lanterns at Low Tide: The Silent Ledger Beneath Each Table."

The documentary will explore the numerous consequences of our practice of commodifying animals for food. These consequences include:

* Cultural impact (global hunger, conflict and war, disease and health epidemics, waste.)
* Ecological toll (soil erosion, water &air pollution, rain forest devastation, global warming, species extinction, ocean destruction, etc.)
* Economic devastation (dependency on resources, health care & pharmaceutical/medical industry.)
Historical issues (cultural aggression, rise of the elite, slavery, domination of women.)
* Personal psyche (commodification of life, disconnectedness from and repression of our innate compassionate nature, intelligence, and sense of justice.)

The film will represent the ideals of kindness, justice, and freedom, and educate on the the keys to awakening from the invisible cultural food trance, and overall, be a vehicle to encourage awakening and living with awareness.

As per the film's title, we want the poster to convey the multi-layered global consequences of animal agriculture without openly attacking the meat industry or people eating animal-sourced foods.

This is a mass-appeal documentary intended to open the eyes of the general public without judgment or alienation of any sector of society. This is not about blame; it's about awareness. The poster should convey the same non-judgmental perspective.

Format should be standard film poster.
Copy for the poster must include the title, sub-title and a quote
Title: Lanterns at Low Tide:
Sub-title: The Silent Ledger Beneath Each Table
Quote options (Pick one) -
As we sow, so shall we reap.
Question everything.
We are all in this together.
None of us is completely innocent.

```html
<!DOCTYPE html>
<html lang="en">
<head>
<meta charset="utf-8">
<title>Lanterns at Low Tide: The Silent Ledger Beneath Each Table</title>
<link rel="stylesheet" href="https://fonts.googleapis.com/css2?family=Bebas+Neue&family=Gochi+Hand&family=Roboto:wght@400&display=swap">
<style>
  :root {
    --rust: #a84525;
    --rust-deep: #6e2a14;
    --sand: #d9cab0;
    --tan-icon: #c5ab7f;
    --ink: #111111;
    --slate: #444444;
  }
  html, body {
    margin: 0;
    padding: 0;
    overflow: hidden;
    background: var(--rust);
  }
  .poster {
    position: relative;
    width: 849px;
    height: 1200px;
    overflow: hidden;
    background: var(--rust);
  }
  .poster__sheet,
  .poster__art {
    position: absolute;
    inset: 0;
  }
  .poster__tagline {
    position: absolute;
    top: 78px;
    left: 0;
    width: 849px;
    margin: 0;
    text-align: center;
    font-family: "Roboto", Arial, sans-serif;
    font-size: 18px;
    letter-spacing: 0.3px;
    color: var(--slate);
  }
  .poster__title {
    position: absolute;
    top: 912px;
    left: 0;
    width: 849px;
    margin: 0;
    text-align: center;
    font-family: "Gochi Hand", "Comic Sans MS", cursive;
    font-weight: 400;
    font-size: 68px;
    line-height: 1;
    text-transform: uppercase;
    color: var(--ink);
    letter-spacing: 1px;
    transform: scaleY(1.38);
    transform-origin: top center;
  }
  .poster__title-small {
    font-size: 34px;
    text-transform: lowercase;
  }
  .poster__subtitle {
    position: absolute;
    top: 990px;
    left: 0;
    width: 849px;
    margin: 0;
    text-align: center;
    font-family: "Bebas Neue", Impact, sans-serif;
    font-weight: 400;
    font-size: 38px;
    line-height: 1;
    color: var(--rust);
    letter-spacing: 0.5px;
  }
</style>
</head>
<body>
<main class="poster">
  <svg class="poster__sheet" width="849" height="1200" viewBox="0 0 849 1200" aria-hidden="true">
    <polygon points="14,6 822,0 849,1140 849,1172 0,1196 0,600" fill="var(--sand)"/>
  </svg>

  <p class="poster__tagline">WE ARE ALL IN THIS TOGETHER.</p>

  <svg class="poster__art" width="849" height="1200" viewBox="0 0 849 1200">
    <defs>
      <linearGradient id="globe-tone" x1="0.25" y1="0.15" x2="0.8" y2="0.95">
        <stop offset="0" stop-color="#cfb596"/>
        <stop offset="0.35" stop-color="#c07a58"/>
        <stop offset="0.65" stop-color="#a84525"/>
        <stop offset="1" stop-color="#b98a6a"/>
      </linearGradient>
      <radialGradient id="globe-rim" cx="0.5" cy="0.5" r="0.5">
        <stop offset="0.82" stop-color="#6e2a14" stop-opacity="0"/>
        <stop offset="1" stop-color="#6e2a14" stop-opacity="0.55"/>
      </radialGradient>
    </defs>

    <g class="icon-paw" role="img" aria-label="Paw print symbol" fill="var(--tan-icon)">
      <ellipse cx="424" cy="202" rx="19" ry="16"/>
      <ellipse cx="401" cy="184" rx="7" ry="9"/>
      <ellipse cx="416" cy="172" rx="7" ry="9"/>
      <ellipse cx="433" cy="172" rx="7" ry="9"/>
      <ellipse cx="448" cy="184" rx="7" ry="9"/>
    </g>

    <g class="globe" role="img" aria-label="Cut-out globe showing the continents of the Americas in sand against a rust ocean">
      <circle cx="424" cy="486" r="236" fill="url(#globe-tone)"/>
      <circle cx="424" cy="486" r="236" fill="url(#globe-rim)"/>
    </g>

    <path class="icon-heart" d="M110 516 L81 487 A16 16 0 0 1 110 467 A16 16 0 0 1 139 487 Z" fill="var(--tan-icon)"/>

    <g class="icon-peace" fill="none" stroke="var(--tan-icon)" stroke-width="5">
      <circle cx="706" cy="496" r="28"/>
      <line x1="706" y1="468" x2="706" y2="524"/>
      <line x1="706" y1="496" x2="686" y2="516"/>
      <line x1="706" y1="496" x2="726" y2="516"/>
    </g>

    <g class="icon-hand" role="img" aria-label="Open hand symbol" fill="var(--tan-icon)" transform="rotate(14 424 770)">
      <rect x="405" y="762" width="36" height="36" rx="14"/>
      <rect x="405" y="742" width="7" height="30" rx="3.5"/>
      <rect x="414" y="735" width="7" height="36" rx="3.5"/>
      <rect x="423" y="737" width="7" height="34" rx="3.5"/>
      <rect x="432" y="743" width="7" height="28" rx="3.5"/>
      <rect x="440" y="762" width="7" height="24" rx="3.5" transform="rotate(40 443 774)"/>
    </g>
  </svg>

  <h1 class="poster__title">Lanterns <span class="poster__title-small">at</span> Low Tide:</h1>
  <h2 class="poster__subtitle">THE SILENT LEDGER BENEATH EACH TABLE</h2>
</main>
</body>
</html>
```